Book cover for a feel-good story

Creation of a cover for the book: "A sparrow under the stairs"

Title: "A sparrow under the stairway" (The English translation should not appear)
Author: "Maelle Durtrand"
Publisher: "Editions Varnou" (should be at the bottom of the page)
Format: 14 x 20.5 cm

The story :
A young single woman (32 years old) is a blogger, she has a passion for shoes.
She has pink hair, just because she likes it. She loves flowers

The text is a humorous story of the woman and the relationship with her mother, similar to Harriet Quill stories.
A feel good text +++

(The words "diamond" and "shoe box" are not keyword, they do not call for representation in the image. They are just a citation from the book)

Enclosed (joined files): examples of styles' cover that would have suited.

Target Market(s)

Teenagers, young adults

Industry/Entity Type

Book

Requirements
Must have
• shoes, pink hair, flowers
Should not have
• Diamond, box of shoes

```html
<!DOCTYPE html>
<html lang="fr">
<head>
<meta charset="utf-8">
<title>Un moineau sous l'escalier — Maelle Durtrand</title>
<link rel="stylesheet" href="https://fonts.googleapis.com/css2?family=League+Spartan:wght@400;700;800&family=Josefin+Sans:wght@600;700&family=Open+Sans:wght@400&display=swap">
<style>
  :root {
    --apricot: #ffc060;
    --apricot-soft: #ffc86b;
    --tangerine: #ff7300;
    --title-light: #ffc35e;
    --paper: #ffffff;
    --ink: #151515;
    --publisher: #f5b84a;
    --illustration-pink: #e0316a;
    --illustration-violet: #7a6ee8;
  }
  * { margin: 0; padding: 0; box-sizing: border-box; }
  html, body { width: 1200px; height: 819px; overflow: hidden; background: var(--paper); }
  .cover {
    position: relative;
    width: 1200px;
    height: 819px;
    overflow: hidden;
    font-family: "League Spartan", sans-serif;
  }

  /* Back cover + spine */
  .back {
    position: absolute;
    left: 0; top: 0;
    width: 639px; height: 819px;
    background: var(--apricot);
  }
  .back-title {
    position: absolute;
    left: 150px; top: 62px;
    width: 270px;
    line-height: 1;
  }
  .back-title .strong {
    display: block;
    color: var(--tangerine);
    font-weight: 800;
    font-size: 41px;
    letter-spacing: 0.5px;
    margin-bottom: 4px;
  }
  .back-title .light {
    display: block;
    color: var(--paper);
    font-weight: 400;
    font-size: 58px;
    margin-top: 6px;
  }
  .blurb {
    position: absolute;
    left: 57px; top: 270px;
    width: 444px;
    font-family: "Open Sans", sans-serif;
    font-size: 12.6px;
    line-height: 22.7px;
    color: var(--paper);
    text-align: justify;
  }
  .blurb p + p { margin-top: 22.7px; }
  .blurb .lead { text-align: center; }

  .spine-title {
    position: absolute;
    left: 586px; top: 34px;
    writing-mode: vertical-rl;
    font-size: 30px;
    line-height: 1;
    letter-spacing: 0.3px;
    white-space: nowrap;
  }
  .spine-title .strong { color: var(--tangerine); font-weight: 800; }
  .spine-title .light { color: var(--paper); font-weight: 400; }

  /* Front cover */
  .front {
    position: absolute;
    left: 639px; top: 0;
    width: 561px; height: 819px;
    background: var(--paper);
    overflow: hidden;
  }
  .front-sun { position: absolute; left: 0; top: 0; }
  .front-title {
    position: absolute;
    left: 48px; top: 50px;
    line-height: 1;
  }
  .front-title .strong {
    display: block;
    color: var(--tangerine);
    font-weight: 800;
    font-size: 78px;
    letter-spacing: 0.5px;
    margin-bottom: 2px;
  }
  .front-title .light {
    display: block;
    color: var(--title-light);
    font-weight: 400;
    font-size: 118px;
    margin-top: 10px;
  }
  .portrait-art {
    position: absolute;
    left: 58px; top: 379px;
    width: 448px; height: 334px;
    border-radius: 46% 54% 48% 52% / 55% 45% 55% 45%;
    background:
      radial-gradient(ellipse at 30% 25%, var(--illustration-violet) 0%, rgba(122,110,232,0) 45%),
      radial-gradient(ellipse at 28% 65%, var(--illustration-pink) 0%, rgba(224,49,106,0) 42%),
      radial-gradient(ellipse at 72% 45%, #f7a8c6 0%, rgba(247,168,198,0) 60%),
      #fbe3ea;
    opacity: 0.9;
  }
  .author {
    position: absolute;
    left: 0; top: 728px;
    width: 561px;
    text-align: center;
    font-family: "Josefin Sans", sans-serif;
    font-weight: 600;
    font-size: 33px;
    letter-spacing: 7px;
    color: var(--ink);
  }
  .publisher {
    position: absolute;
    left: 0; top: 773px;
    width: 561px;
    text-align: center;
    font-family: "Josefin Sans", sans-serif;
    font-weight: 700;
    font-size: 15px;
    letter-spacing: 2.4px;
    color: var(--publisher);
  }
</style>
</head>
<body>
<main class="cover">

  <section class="back">
    <h2 class="back-title">
      <span class="strong">UN MOINEAU</span>
      <span class="strong">SOUS L'</span>
      <span class="light">ESCALIER</span>
    </h2>

    <div class="blurb">
      <p class="lead">A young single woman (32 years old) is a blogger, she has a passion for shoes. She has pink hair, just because she likes it. She loves flowers</p>
      <p>The text is a humorous story of the woman and the relationship with her mother, similar to Harriet Quill stories. A feel good text +++ (The words "diamond" and "shoe box" are not keyword, they do not call for representation in the image. They are just a citation from the book) Enclosed (joined files): examples of styles' cover that would have suited.</p>
      <p>The text is a humorous story of the woman and the relationship with her mother, similar to Harriet Quill stories. A feel good text +++ (The words "diamond" and "shoe box" are not keyword, they do not call for representation in the image. They are just a citation from the book) Enclosed (joined files): examples of styles' cover that would have suited.</p>
      <p>The text is a humorous story of the woman and the relationship with her mother, similar to Harriet Quill stories. A feel good text +++ (The words "diamond" and "shoe box" are not keyword, they do not call for representation in the image. They are just a citation from the book) Enclosed (joined files): examples of styles' cover that would have suited.</p>
    </div>

    <div class="spine-title">
      <span class="strong">UN MOINEAU SOUS L'</span>
      <span class="light">ESCALIER</span>
    </div>
  </section>

  <section class="front">
    <svg class="front-sun" width="561" height="240" viewBox="0 0 561 240" aria-hidden="true">
      <circle cx="369" cy="18" r="200" fill="var(--apricot-soft)"/>
    </svg>

    <h1 class="front-title">
      <span class="strong">UN MOINEAU</span>
      <span class="strong">SOUS L'</span>
      <span class="light">ESCALIER</span>
    </h1>

    <div class="portrait-art" role="img" aria-label="Watercolour illustration of a young woman with pink hair, eyes closed, crowned and surrounded by violet, pink and yellow flowers with scattered petals"></div>

    <p class="author">MAELLE DURTRAND</p>
    <p class="publisher">EDITIONS VARNOU</p>
  </section>

</main>
</body>
</html>
```